Website for the new investment company.

We are building a website for a new company. This will be an investment company. The name of the company is Tern Harbor Equity, or THE. We don't have a company logo yet, so happy to take suggestions on that as well (and will add that to the final cost). The investors of this company will exclusively be Dunmore College alumni graduates. The investors are not students, but instead older professionals in various industries, that previously graduated from the Dunmore College. This company will establish an investment fund and invest in multiple businesses.
The purpose of the website will be to educate Dunmore alumni on the investment fund.
We are looking for:
1. The design to be relatable, but not the copy of the Dunmore College website. https://www.dunmorecol.edu/
2. This is an investment website and must mimic other similar websites
https://plovergate-fund.com/
https://www.brindlevest.com/
https://kestowholdings.com/site/global/home/p_home.gsp
3. Project timeline. We are focused on receiving a design in the next two weeks and then finishing the website over the following 2 weeks. We anticipate paying for additional work and customization after the designs are provided.
4. Website Pages:
1) Homepage - Mission and Objective (high quality photos along with text that we will provide after selecting the winning design)
2) Background - Text and biographies on the 2 founders (high quality photos along with text that we will provide after selecting the winning design)
3) Advisory Board - Text and biographies on the investment Fund's 3 advisory board members (high quality photos along with text that we will provide after selecting the winning design)
4) Fund I - Text and information on the specific investment fund including pictures and biographies of the investment committee (high quality photos along with text that we will provide after selecting the winning design)
5) Contact Us - Typical website contact page for visitors

Target Market(s)

Dunmore Alumni graduates

Industry/Entity Type

Investment

Coding

Coded - Design and coding required

Font styles to use
Serif
Sans Serif

Colors
0054AA
0677BA
7BADD7
CADEEF
E8F1F8

Requirements
Must have
• Must look like other private investment websites as provided in project description
Nice to have
• Mimics the Dunmore College style, but definitely needs to be different. This company has no direct relationship with Dunmore College.
Should not have
• No commercial transactions, no credit card payments etc. Do not replicate any logos, designs or proprietary content from Dunmore College.

```html
<!DOCTYPE html>
<html lang="en">
<head>
<meta charset="utf-8">
<title>Tern Harbor Equity</title>
<link href="https://fonts.googleapis.com/css2?family=Poppins:wght@400;500;600;700&display=swap" rel="stylesheet">
<style>
:root{
  --blue:#3d5cf5;
  --ink:#111318;
  --grey:#6e6e72;
  --line:#dcdcde;
  --soft:#e3e6fb;
  --white:#ffffff;
}
*{box-sizing:border-box;margin:0;padding:0}
html,body{width:1200px;height:2218px;overflow:hidden;background:var(--white)}
body{position:relative;font-family:'Poppins',sans-serif;color:var(--ink)}
.abs{position:absolute}
a{color:inherit;text-decoration:none}
.btn{position:absolute;display:flex;align-items:center;justify-content:center;background:var(--blue);color:var(--white);font-weight:600;border-radius:30px}

/* hero */
.hero{left:0;top:0;width:1200px;height:646px;background:linear-gradient(120deg,#5b6066 0%,#6d7278 35%,#7c7a80 60%,#8a7f86 80%,#6e6a70 100%)}
.hero-shade{left:0;top:0;width:1200px;height:646px;background:linear-gradient(90deg,rgba(40,44,60,.35),rgba(40,44,60,.05))}
.brand-top{left:83px;top:36px;display:flex;align-items:center;gap:10px;color:var(--white);font-weight:600;font-size:18px}
.brand-top .mark{width:26px;height:26px;background:var(--blue)}
.nav{top:38px;right:83px;display:flex;gap:50px;color:var(--white);font-size:17px}
.hero-title{left:83px;top:206px;width:660px;color:var(--white);font-size:51px;line-height:59px;font-weight:700}
.hero-sub{left:83px;top:401px;width:630px;color:var(--white);font-size:17px;line-height:25px}

/* who */
.who-card{left:84px;top:697px;width:207px;height:208px;background:var(--blue);border-radius:34px;color:var(--white)}
.who-card h3{position:absolute;left:17px;top:85px;font-size:20px;font-weight:700}
.who-card p{position:absolute;left:17px;top:121px;width:180px;font-size:9.5px;line-height:15px}
.who-photo{left:291px;top:697px;width:209px;height:208px;border-radius:34px;background:linear-gradient(135deg,#c8c6c2,#6a6156 55%,#2c2620)}
.who-rule{left:84px;top:920px;width:416px;height:1px;background:var(--line)}
.who-note{left:141px;top:939px;width:360px;font-size:9.5px;line-height:15px;color:var(--grey)}
.who-text{left:550px;top:696px;width:567px;font-size:16.8px;line-height:25px;text-align:justify}

.divider{left:0;width:1200px;height:2px;background:var(--line)}

/* mission */
.sec-h{font-size:34px;font-weight:600}
.sec-p{width:650px;font-size:16.5px;line-height:25px;color:var(--grey);text-align:justify}
.mission-photo{left:783px;top:1134px;width:334px;height:457px;border-radius:30px;background:linear-gradient(160deg,#c79a72,#a86f48 40%,#d9d3cc 70%,#3a4a6a)}

/* contact */
.vline{left:798px;top:1643px;width:2px;height:240px;background:var(--line)}

/* footer */
.foot-brand{left:84px;top:1928px;color:var(--blue);font-size:22px;font-weight:600;display:flex;align-items:center;gap:10px}
.foot-brand .mark{width:22px;height:22px;background:var(--blue)}
.foot-about{left:84px;top:1987px;width:234px;font-size:11.5px;line-height:17.5px;color:var(--grey);text-align:justify}
.social{top:2055px;width:42px;height:42px;border-radius:50%;background:var(--soft)}
.foot-col h4{font-size:20px;font-weight:600;margin-bottom:14px}
.foot-col li{list-style:none;font-size:16.5px;color:var(--grey);height:35px}
.news-p{left:880px;top:1967px;width:200px;font-size:11.5px;line-height:17.5px;color:var(--grey)}
.news-input{left:880px;top:2018px;width:209px;height:34px;border-radius:17px;background:#f2f2f4;font-size:11.5px;color:var(--grey);padding:9px 9px}
.copy{left:0;top:2182px;width:1200px;text-align:center;font-size:13px;color:var(--grey)}
</style>
</head>
<body>

<section class="abs hero" role="img" aria-label="Blurred photo of sticky notes pinned to a board"></section>
<div class="abs hero-shade"></div>
<div class="abs brand-top"><span class="mark"></span>Tern Harbor Equity</div>
<nav class="abs nav"><a>Values</a><a>Investments</a><a>Founder</a><a>Connect</a><a>About</a></nav>
<h1 class="abs hero-title">Connecting Dunmore Alumni Through Strategic Investments</h1>
<p class="abs hero-sub">Fostering growth and success among Dunmore College alumni through collaborative investments.</p>
<a class="btn" style="left:84px;top:485px;width:229px;height:52px;font-size:16.5px">Discover Our Mission</a>

<div class="abs who-card">
  <svg class="abs" style="left:154px;top:34px" width="22" height="22" viewBox="0 0 22 22" fill="none" stroke="#fff" stroke-width="2.4"><path d="M4 18L18 4M7 4h11v11"/></svg>
  <h3>Who We Are</h3>
  <p>Founded by Dunmore College graduates, THE brings together seasoned professionals dedicated to making a difference.</p>
</div>
<div class="abs who-photo" role="img" aria-label="Photo of professionals writing notes at a meeting table"></div>
<div class="abs who-rule"></div>
<svg class="abs" style="left:84px;top:938px" width="42" height="44" viewBox="0 0 42 44"><circle cx="20" cy="25" r="17" fill="none" stroke="#111" stroke-width="1.2"/><circle cx="24" cy="18" r="16" fill="#111"/></svg>
<p class="abs who-note">Lorem ipsum dolor sit amet, consectetur adipiscing elit. Cras lacus ex, interdum sit amet dignissim sed, consequat ultricies velit. Vivamus sed sem in est sollicitudin pharetra.</p>
<p class="abs who-text">Lorem ipsum dolor sit amet, consectetur adipiscing elit. Cras lacus ex, interdum sit amet dignissim sed, consequat ultricies velit. Vivamus sed sem in est sollicitudin pharetra. Suspendisse fringilla justo commodo orci imperdiet consequat. Fusce vitae dui ut enim pulvinar convallis. Maecenas consectetur fermentum urna, nec consequat dui ullamcorper id. Donec maximus tortor bibendum odio ornare consequat suscipit at nisl. Fusce maximus tortor sit amet turpis tincidunt suscipit.</p>
<a class="btn" style="left:550px;top:930px;width:147px;height:52px;font-size:16.5px">Learn More</a>

<div class="abs divider" style="top:1083px"></div>

<h2 class="abs sec-h" style="left:84px;top:1182px">Our Mission</h2>
<p class="abs sec-p" style="left:84px;top:1246px">Lorem ipsum dolor sit amet, consectetur adipiscing elit. Cras lacus ex, interdum sit amet dignissim sed, consequat ultricies velit. Vivamus sed sem in est sollicitudin pharetra. Suspendisse fringilla justo commodo orci imperdiet consequat. Fusce vitae dui ut enim pulvinar convallis.</p>
<h2 class="abs sec-h" style="left:84px;top:1382px">Our Goals</h2>
<p class="abs sec-p" style="left:84px;top:1446px">Lorem ipsum dolor sit amet, consectetur adipiscing elit. Cras lacus ex, interdum sit amet dignissim sed, consequat ultricies velit. Vivamus sed sem in est sollicitudin pharetra. Suspendisse fringilla justo commodo orci imperdiet consequat. Fusce vitae dui ut enim pulvinar convallis.</p>
<div class="abs mission-photo" role="img" aria-label="Photo of two colleagues discussing plans at a whiteboard in a brick office"></div>

<div class="abs divider" style="top:1642px"></div>
<div class="abs vline"></div>
<h2 class="abs" style="left:84px;top:1695px;font-size:42px;font-weight:600">Get in Touch</h2>
<p class="abs sec-p" style="left:84px;top:1768px;width:667px;font-size:17px">We'd love to hear from you. Reach out to us for more information about our fund, investment opportunities, or any other inquiries.</p>
<p class="abs" style="left:880px;top:1712px;width:238px;text-align:center;font-size:20px;color:var(--grey)">Connect With Us</p>
<a class="btn" style="left:917px;top:1760px;width:166px;height:52px;font-size:16.5px">Connect Now</a>

<div class="abs divider" style="top:1882px"></div>

<div class="abs foot-brand"><span class="mark"></span>Tern Harbor Equity</div>
<p class="abs foot-about">Lorem ipsum dolor sit amet, consectetur adipiscing elit. Praesent quis tristique enim.</p>
<span class="abs social" style="left:84px"></span>
<span class="abs social" style="left:147px"></span>
<span class="abs social" style="left:211px"></span>
<span class="abs social" style="left:275px"></span>

<div class="abs foot-col" style="left:417px;top:1920px"><h4>Other Pages</h4><ul><li>About</li><li>Contact</li><li>Values</li><li>Investment</li><li>Founder</li></ul></div>
<div class="abs foot-col" style="left:642px;top:1920px"><h4>Quick Links</h4><ul><li>Privacy Policy</li><li>Terms Of Service</li><li>Disclaimer</li><li>Credits</li><li>FAQ</li></ul></div>
<div class="abs foot-col" style="left:880px;top:1920px"><h4>Newsletter</h4></div>
<p class="abs news-p">Lorem ipsum dolor sit amet, consectetur adipiscing elit.</p>
<div class="abs news-input">Your email</div>
<a class="btn" style="left:880px;top:2062px;width:209px;height:34px;font-size:11.5px">Subscribe</a>

<div class="abs divider" style="top:2162px"></div>
<p class="abs copy">©2024 Tern Harbor Equity. All rights reserved.</p>

</body>
</html>
```